New Architectural Firm Business Cards

New Business card to compliment previous pixel forum logo (attached). Please design a business card that is simple, modern, creative....please do not use "symbols", simply the logo and associated graphics/text. The front should contain name/address/phone/email/web address (with graphics).....back should be 100% graphic design using the logo somehow. Hoping for a two color (black and yellow) design. full bleed design, no borders

Target Market(s)

Commercial Architecture Clients

Industry/Entity Type

Architecture

Contact Information for Business Card

Please design a business card that is simple, modern, creative....please do not use "symbols", simply the logo and associated graphics/text. The front should contain name/address/phone/email/web address (with graphics).....back should be 100% graphic design using the logo somehow

Font styles to use
Sans Serif

Colors
FFF300
FFF600
FEFA6F
FFFEC7
FFFEE8

Requirements
Must have
• Clean, Modern Design
Should not have
• Stock images or "icons"

```html
<!DOCTYPE html>
<html lang="en">
<head>
<meta charset="utf-8">
<title>Halden Architecture – Business Cards</title>
<link href="https://fonts.googleapis.com/css2?family=Montserrat:wght@600;700;800&family=Open+Sans:wght@400;600&display=swap" rel="stylesheet">
<style>
  :root {
    --brand-yellow: #F7C414;
    --ink: #1E1E1E;
    --paper: #FFFFFF;
    --backdrop: #2B2B2D;
  }
  * { box-sizing: border-box; margin: 0; padding: 0; }
  html, body { width: 1200px; height: 900px; overflow: hidden; }
  body {
    background: var(--backdrop);
    position: relative;
    font-family: "Open Sans", Arial, sans-serif;
  }
  .card {
    position: absolute;
    width: 700px;
    height: 400px;
    border-radius: 22px;
    box-shadow: 0 14px 30px rgba(0,0,0,0.45);
  }
  .card--back {
    left: 340px; top: 40px;
    background: var(--brand-yellow);
    display: flex; align-items: center; justify-content: center;
  }
  .card--front {
    left: 160px; top: 460px;
    background: var(--paper);
    color: var(--ink);
  }
  .wordmark {
    display: flex; align-items: center; gap: 18px;
    font-family: "Montserrat", Arial, sans-serif;
    font-weight: 800;
    letter-spacing: 0.02em;
    line-height: 1;
  }
  .wordmark__dot { border-radius: 50%; flex: none; }
  .card--back .wordmark { color: var(--ink); font-size: 40px; }
  .card--back .wordmark__dot { width: 54px; height: 54px; background: var(--paper); }
  .wordmark__stack { display: flex; flex-direction: column; gap: 8px; }
  .wordmark__sub { font-size: 0.62em; letter-spacing: 0.08em; }

  .card--front .wordmark {
    position: absolute; right: 44px; bottom: 46px;
    color: var(--brand-yellow); font-size: 34px;
  }
  .card--front .wordmark__dot { width: 44px; height: 44px; background: var(--brand-yellow); }

  .holder { position: absolute; left: 60px; top: 44px; }
  .holder__name {
    font-family: "Montserrat", Arial, sans-serif;
    font-weight: 800; font-size: 30px;
    color: var(--brand-yellow); letter-spacing: 0.02em;
  }
  .holder__title { font-size: 18px; margin-top: 2px; }
  .rule {
    position: absolute; left: 60px;
    width: 58px; height: 3px; background: var(--brand-yellow);
  }
  .rule--first { top: 148px; }
  .rule--second { top: 262px; }
  .address {
    position: absolute; left: 60px; top: 176px;
    font-size: 19px; line-height: 1.45;
  }
  .contacts {
    position: absolute; left: 60px; top: 290px;
    list-style: none; font-size: 19px; line-height: 1.5;
  }
  .contacts li { display: flex; align-items: center; gap: 10px; }
  .contacts svg { width: 16px; height: 16px; flex: none; }
</style>
</head>
<body>

  <section class="card card--back" aria-label="Card back">
    <div class="wordmark">
      <span class="wordmark__dot"></span>
      <span class="wordmark__stack">
        <span>HALDEN</span>
        <span class="wordmark__sub">ARCHITECTURE</span>
      </span>
    </div>
  </section>

  <section class="card card--front" aria-label="Card front">
    <div class="holder">
      <h1 class="holder__name">MARLO QUINN</h1>
      <p class="holder__title">Director</p>
    </div>
    <span class="rule rule--first"></span>
    <address class="address" style="font-style:normal">
      2270 Ridgeline Ave,<br>Fairbrook, Oregon 97401
    </address>
    <span class="rule rule--second"></span>
    <ul class="contacts">
      <li>
        <svg viewBox="0 0 16 16" aria-hidden="true"><rect x="4" y="1" width="8" height="14" rx="1.5" fill="none" stroke="#F7C414" stroke-width="1.5"/><line x1="7" y1="12.5" x2="9" y2="12.5" stroke="#F7C414" stroke-width="1.5"/></svg>
        555-214-0836
      </li>
      <li>
        <svg viewBox="0 0 16 16" aria-hidden="true"><rect x="1" y="3" width="14" height="10" fill="#F7C414"/><polyline points="1,3 8,9 15,3" fill="none" stroke="#fff" stroke-width="1.3"/></svg>
        info@haldenarch.com
      </li>
      <li>
        <svg viewBox="0 0 16 16" aria-hidden="true"><circle cx="8" cy="8" r="6.5" fill="none" stroke="#F7C414" stroke-width="1.4"/><ellipse cx="8" cy="8" rx="3" ry="6.5" fill="none" stroke="#F7C414" stroke-width="1.2"/><line x1="1.5" y1="8" x2="14.5" y2="8" stroke="#F7C414" stroke-width="1.2"/></svg>
        www.haldenarch.com
      </li>
    </ul>
    <div class="wordmark">
      <span class="wordmark__dot"></span>
      <span class="wordmark__stack">
        <span>HALDEN</span>
        <span class="wordmark__sub">ARCHITECTURE</span>
      </span>
    </div>
  </section>

</body>
</html>
```